Medical device box for kits used for self testing purposes. Attractive simplistic design

Looking for a design that will go on a box that offer multiple range of medical testing ranging from hormones panel to diabetes and thyroid hormones. looking for something attractive and simple to go on a box 6 x 4.5 x 1 inches. attached are some examples from competitors. and our logo that be incorporated with the design.
Picture of the boxes have been attached, pick the color you think goes best with your design.

Target Market(s)

Patients and regular consumers

Industry/Entity Type

Medical

Requirements
Nice to have
• Simple design that is eye catching

```html
<!DOCTYPE html>
<html lang="en">
<head>
<meta charset="utf-8">
<title>Food Sensitivity Comprehensive Test – Box Lid</title>
<link href="https://fonts.googleapis.com/css2?family=Archivo:wght@800&family=Fira+Sans:ital,wght@0,400;0,600;0,700;1,400&display=swap" rel="stylesheet">
<style>
  :root {
    --backdrop: #c4e2e6;
    --paper: #f6f7f7;
    --royal: #4565c4;
    --royal-deep: #2c4aa8;
    --navy: #263f8c;
    --sky-edge: #4a9fd8;
    --ink: #111111;
    --white: #ffffff;
  }
  * { margin: 0; padding: 0; box-sizing: border-box; }
  html, body {
    width: 1200px;
    height: 952px;
    overflow: hidden;
    background: var(--backdrop);
  }
  .lid {
    position: absolute;
    left: 100px;
    top: 101px;
    width: 1000px;
    height: 750px;
    background: var(--paper);
    overflow: hidden;
    box-shadow: 0 6px 18px rgba(30, 60, 90, 0.18);
  }
  .lid-field {
    position: absolute;
    inset: 0;
  }
  .brand {
    position: absolute;
    right: 70px;
    top: 40px;
    display: flex;
    align-items: center;
    gap: 14px;
  }
  .brand-dot {
    width: 34px;
    height: 34px;
    border-radius: 50%;
    background: var(--navy);
  }
  .brand-name {
    font-family: "Fira Sans", sans-serif;
    font-weight: 700;
    font-size: 54px;
    color: var(--navy);
    letter-spacing: 1px;
  }
  .title {
    position: absolute;
    left: 70px;
    top: 262px;
    width: 570px;
    font-family: "Archivo", sans-serif;
    font-weight: 800;
    font-size: 43px;
    line-height: 1.02;
    color: var(--ink);
    letter-spacing: 1px;
    white-space: nowrap;
  }
  .panel-tag {
    position: absolute;
    left: 70px;
    top: 446px;
    font-family: "Fira Sans", sans-serif;
    font-weight: 600;
    font-size: 36px;
    line-height: 1.2;
    color: var(--white);
    white-space: nowrap;
  }
  .blurb {
    position: absolute;
    left: 90px;
    top: 528px;
    width: 540px;
    font-family: "Fira Sans", sans-serif;
    font-size: 19px;
    line-height: 1.3;
    color: var(--white);
  }
  .feature {
    position: absolute;
    display: flex;
    align-items: center;
    gap: 18px;
    font-family: "Fira Sans", sans-serif;
    font-size: 16px;
    color: var(--white);
  }
  .feature::before {
    content: "";
    width: 40px;
    height: 32px;
    border-radius: 50%;
    background: var(--white);
  }
  .feature-one { left: 110px; top: 650px; }
  .feature-two { left: 410px; top: 620px; }
</style>
</head>
<body>
  <main class="lid">
    <svg class="lid-field" width="1000" height="750" viewBox="0 0 1000 750" aria-hidden="true">
      <polygon points="0,420 650,420 650,300 1000,300 1000,750 0,750" fill="var(--royal)"/>
      <rect x="0" y="430" width="655" height="74" fill="var(--navy)"/>
      <g class="cross" transform="translate(830 290)">
        <path d="M-62,-165 H62 V-62 H165 V62 H62 V165 H-62 V62 H-165 V-62 H-62 Z" fill="var(--white)"/>
        <path d="M-50,-150 H50 V-50 H150 V50 H50 V150 H-50 V50 H-150 V-50 H-50 Z" fill="var(--navy)" stroke="var(--sky-edge)" stroke-width="4"/>
        <path d="M-26,-112 H26 V-26 H112 V26 H26 V112 H-26 V26 H-112 V-26 H-26 Z" fill="var(--white)"/>
      </g>
    </svg>

    <div class="brand">
      <span class="brand-dot"></span>
      <span class="brand-name">Veridia</span>
    </div>

    <h1 class="title">FOOD SENSITIVITY<br>COMPREHENSIVE TEST</h1>

    <p class="panel-tag">Diabetes and thyroid hormones</p>

    <p class="blurb">Lorem ipsum dolor sit amet, consectetuer adipiscing elit.<br>Maecenas porttitor congue massa.</p>

    <p class="feature feature-one">Lorem ipsum</p>
    <p class="feature feature-two">Lorem ipsum</p>
  </main>
</body>
</html>
```